A new healing and spiritual podcast needs a design.

We need a design for the podcast that will also be used on the supporting website. The name is Still Lantern Path. The podcast will be about tapping into our own guidance to have a great life. There will be interviews, meditations, discussions on all aspects of energy healing and alternative healing techniques. The website will be where classes will be offered. Looking for something that conveys a peaceful feeling without looking too "healy-feely". Yet also want it to get peoples attention.

Target Market(s)

Metaphysical, spiritual (not religious), energy healers

Font styles to use
Serif

Requirements
Must have
• The name "Still Lantern Path"
Nice to have
• I'd like it to be inviting, catch peoples eye, convey a peaceful feeling, yet not be boring.
Should not have
• Animated (like comic strip) images.

```html
<!DOCTYPE html>
<html lang="en">
<head>
<meta charset="utf-8">
<title>Still Lantern Path</title>
<link rel="stylesheet" href="https://fonts.googleapis.com/css2?family=Playfair+Display:wght@700;900&family=Lora:wght@400&display=swap">
<style>
  :root {
    --page: #ffffff;
    --white: #ffffff;
    --navy: #1d3650;
    --ink: #1f2a38;
    --cosmos-deep: #0d1230;
    --cosmos-blue: #3048a8;
    --cosmos-glow: #6d7fd6;
    --cosmos-amber: #8a4a26;
    --dawn-cream: #f3e4d2;
    --dawn-peach: #f2c9a4;
    --dawn-rose: #e6bfb8;
    --shore-teal: #4f7a73;
    --shore-dark: #2f463f;
  }
  * { margin: 0; padding: 0; box-sizing: border-box; }
  html, body {
    width: 1200px;
    height: 2322px;
    overflow: hidden;
    background: var(--page);
  }
  .canvas {
    position: relative;
    width: 1200px;
    height: 2322px;
  }
  .post {
    position: absolute;
    left: 132px;
    width: 1000px;
    height: 1000px;
    overflow: hidden;
  }
  .post--cosmic { top: 132px; }
  .post--dawn { top: 1244px; }

  .photo {
    position: absolute;
    inset: 0;
  }
  .photo--cosmic {
    background:
      radial-gradient(ellipse 30% 28% at 48% 32%, rgba(232,180,160,0.75), transparent 70%),
      radial-gradient(ellipse 18% 16% at 26% 28%, rgba(200,60,110,0.55), transparent 70%),
      radial-gradient(ellipse 40% 45% at 78% 35%, var(--cosmos-glow), transparent 75%),
      radial-gradient(ellipse 35% 55% at 15% 60%, var(--cosmos-amber), transparent 75%),
      radial-gradient(ellipse 60% 50% at 50% 65%, var(--cosmos-blue), transparent 80%),
      linear-gradient(180deg, #1a2150 0%, var(--cosmos-deep) 100%);
  }
  .photo--dawn {
    background:
      radial-gradient(ellipse 35% 40% at 35% 45%, rgba(255,245,225,0.9), transparent 75%),
      linear-gradient(180deg, var(--dawn-cream) 0%, var(--dawn-peach) 45%, var(--dawn-rose) 70%, var(--shore-teal) 88%, var(--shore-dark) 100%);
  }

  .title {
    font-family: "Playfair Display", Georgia, serif;
    font-weight: 900;
    text-transform: uppercase;
    letter-spacing: 0;
  }
  .post--cosmic .title {
    position: absolute;
    top: 712px;
    left: 0;
    width: 1000px;
    text-align: center;
    color: var(--white);
    font-size: 70px;
    line-height: 1;
  }
  .post--cosmic .tagline {
    position: absolute;
    top: 828px;
    left: 0;
    width: 1000px;
    text-align: center;
    font-family: "Playfair Display", Georgia, serif;
    font-weight: 700;
    text-transform: uppercase;
    color: var(--white);
    font-size: 29px;
    line-height: 49px;
    letter-spacing: 0.5px;
  }

  .post--dawn .title {
    position: absolute;
    top: 56px;
    left: 50px;
    color: var(--navy);
    font-size: 72px;
    line-height: 82px;
  }
  .post--dawn .rule {
    position: absolute;
    left: 533px;
    top: 78px;
    width: 6px;
    height: 222px;
    border-radius: 3px;
    background: var(--navy);
  }
  .post--dawn .intro {
    position: absolute;
    top: 64px;
    left: 597px;
    width: 370px;
    font-family: "Lora", Georgia, serif;
    font-weight: 400;
    font-size: 30px;
    line-height: 48px;
    color: var(--ink);
  }
</style>
</head>
<body>
  <main class="canvas">
    <section class="post post--cosmic">
      <div class="photo photo--cosmic" role="img" aria-label="Woman with closed eyes blended into a starry blue galaxy and nebula"></div>
      <h1 class="title">Still Lantern Path</h1>
      <p class="tagline">Interviews, meditations and healing wisdom<br>to light the guidance within you</p>
    </section>

    <section class="post post--dawn">
      <div class="photo photo--dawn" role="img" aria-label="Man seen from behind with arms raised toward a hazy sunrise over a bay with rocky islands"></div>
      <h2 class="title">Still<br>Lantern<br>Path</h2>
      <div class="rule"></div>
      <p class="intro">Conversations on energy healing, meditation and trusting your own inner guidance.</p>
    </section>
  </main>
</body>
</html>
```